Book Cover for College Series

We need an e-book cover design for a collection of poetry entitled, "Chalk Lanterns Vol. 1: The Heartland." Although the price is set to $200, whomever I select for this project will be used for the next three volumes of the series in the future. So be sure to have contact information ready if selected.
If selected, we can be reached at BrightQuillPress@mailnest.example
Be sure to check out the Look and Feel Slider. We would like it to come across as serious and professional, yet very personable and modern.
Target Market(s)
Target market is both current college students as well as former college students (University alums). However, on some level it is marketed towards anyone associated with universities, including professors, as well as poetry readers. Which is why, although personable, We need the look to have a serious feel to it as well.
Industry/Entity Type
College
Requirements
Must have
- The title of the book: "Chalk Lanterns: Vol 1. The Heartland"
- Be sure to have the author's name: Benedict Marlow Tesh
Nice to have
- - Nice to have a design that somehow gives off the feeling of nostalgia.
Optional: Underneath the title, include "A collection of poetry celebrating the top universities of the Midwest."
- Only include the following if it does not get in the way of the feel/look of the cover: Have the initials: B.M.T. on the left-hand corner. An example of how this should appear is in the photo attached However, it does not necessarily need to be this big.

```html
<!DOCTYPE html>
<html lang="en">
<head>
<meta charset="utf-8">
<title>Chalk Lanterns Vol. 1: The Heartland — Cover</title>
<link rel="stylesheet" href="https://fonts.googleapis.com/css2?family=Cinzel:wght@600&family=Josefin+Sans:wght@400;700&family=Open+Sans:wght@700&family=Cormorant+Garamond:wght@500&display=swap">
<style>
  :root {
    --page: #ffffff;
    --cover: #c4cec6;
    --map-top: #5a3a36;
    --map-bottom: #c8711f;
    --ink-white: #ffffff;
    --ink-brown: #5a2c12;
    --ink-black: #1a1a1a;
    --mark: #4d3a3f;
    --shadow: rgba(40, 50, 45, 0.55);
  }
  * { margin: 0; padding: 0; box-sizing: border-box; }
  html, body {
    width: 1200px;
    height: 1000px;
    overflow: hidden;
    background: var(--page);
  }
  .canvas {
    position: relative;
    width: 1200px;
    height: 1000px;
  }
  .cover {
    position: absolute;
    left: 244px;
    top: 24px;
    width: 714px;
    height: 952px;
    background: var(--cover);
    overflow: hidden;
  }
  .region-map {
    position: absolute;
    left: 0;
    top: 0;
    width: 714px;
    height: 640px;
    background: linear-gradient(180deg,
      rgba(90, 58, 54, 0.16) 0%,
      rgba(150, 90, 50, 0.14) 55%,
      rgba(200, 113, 31, 0.10) 85%,
      rgba(200, 113, 31, 0) 100%);
  }
  .imprint {
    position: absolute;
    right: 26px;
    top: 22px;
    display: flex;
    flex-direction: column;
    align-items: center;
    gap: 8px;
  }
  .imprint-dot {
    width: 86px;
    height: 86px;
    border: 3px solid var(--mark);
    border-radius: 50%;
  }
  .imprint-name {
    font-family: "Josefin Sans", sans-serif;
    font-weight: 700;
    font-size: 17px;
    color: var(--mark);
    letter-spacing: 1px;
  }
  .series-title {
    position: absolute;
    right: 40px;
    top: 576px;
    font-family: "Cinzel", serif;
    font-weight: 600;
    font-size: 44px;
    letter-spacing: 3px;
    color: var(--ink-white);
    text-shadow: 3px 4px 6px var(--shadow);
    white-space: nowrap;
  }
  .volume {
    position: absolute;
    right: 42px;
    top: 630px;
    font-family: "Josefin Sans", sans-serif;
    font-weight: 400;
    font-size: 30px;
    color: var(--ink-brown);
    white-space: nowrap;
  }
  .book-title {
    position: absolute;
    left: 30px;
    width: 654px;
    top: 714px;
    text-align: center;
    font-family: "Josefin Sans", sans-serif;
    font-weight: 700;
    font-size: 70px;
    line-height: 1;
    letter-spacing: 0;
    color: var(--ink-white);
    text-shadow: 4px 6px 8px var(--shadow);
    white-space: nowrap;
  }
  .tagline {
    position: absolute;
    left: 0;
    width: 714px;
    top: 796px;
    text-align: center;
    font-family: "Open Sans", sans-serif;
    font-weight: 700;
    font-size: 12.5px;
    color: var(--ink-black);
    white-space: nowrap;
  }
  .author {
    position: absolute;
    left: 0;
    width: 714px;
    top: 874px;
    text-align: center;
    font-family: "Cormorant Garamond", serif;
    font-weight: 500;
    font-size: 25px;
    letter-spacing: 1px;
    color: var(--ink-white);
    white-space: nowrap;
  }
</style>
</head>
<body>
  <main class="canvas">
    <section class="cover">
      <div class="region-map" role="img" aria-label="Distressed outline map of the Midwest states, strokes fading from dark brown to orange"></div>

      <div class="imprint">
        <span class="imprint-dot"></span>
        <span class="imprint-name">B.M.T.</span>
      </div>

      <h2 class="series-title">CHALK LANTERNS</h2>
      <p class="volume">VOL{1}</p>
      <h1 class="book-title">THE HEARTLAND</h1>
      <p class="tagline">A COLLECTION OF POETRY CELEBRATING THE TOP UNIVERSITIES OF THE MIDWEST.</p>
      <p class="author">BENEDICT MARLOW TESH</p>
    </section>
  </main>
</body>
</html>
```